RIVERtide Press Needs a Book Cover Design

We need a book cover design for an inspirational, motivational nugget book. It's another part of a series of small 1-paragraph chapter books with lots of quotes. It is a spiritual book and we would like to see designs that depict peace through a storm. The final design should communicate peace or calm through violent storms of life--adversity, setbacks, and sorrow.
The book size is 5.5 x 8.5 ins and the number of pages is 96.
Updates
Project Deadline Extended
Reason: To be able to allow for more submissions.
Target Market(s)
General reading audience
Look and feel
Each slider illustrates characteristics of the customer's brand and the style your logo design should communicate.

```html
<!DOCTYPE html>
<html lang="en">
<head>
<meta charset="UTF-8">
<title>Peace Through The Storms — Book Cover</title>
<link rel="stylesheet" href="https://fonts.googleapis.com/css2?family=Oswald:wght@600&family=Cormorant+Garamond:ital,wght@1,600&display=swap">
<style>
  :root {
    --page-bg: #ffffff;
    --storm-grey: #8a8986;
    --storm-dark: #5e5c58;
    --mist: #cfcac2;
    --glow-core: #fff3c4;
    --glow-warm: #f2b14a;
    --glow-deep: #c9742a;
    --title-orange: #eea152;
    --script-white: #ffffff;
    --text-shadow: rgba(40, 30, 20, 0.55);
  }
  * { margin: 0; padding: 0; box-sizing: border-box; }
  html, body {
    width: 1200px;
    height: 1200px;
    overflow: hidden;
    background: var(--page-bg);
  }
  .canvas {
    position: relative;
    width: 1200px;
    height: 1200px;
  }
  .book-cover {
    position: absolute;
    left: 270px;
    top: 90px;
    width: 660px;
    height: 1020px;
    overflow: hidden;
  }
  .cover-art {
    position: absolute;
    inset: 0;
    background:
      radial-gradient(ellipse 34% 28% at 52% 58%, var(--glow-core) 0%, rgba(255, 230, 150, 0.85) 35%, rgba(242, 177, 74, 0) 100%),
      radial-gradient(ellipse 60% 45% at 50% 62%, rgba(242, 177, 74, 0.9) 0%, rgba(201, 116, 42, 0.55) 45%, rgba(201, 116, 42, 0) 100%),
      radial-gradient(ellipse 45% 12% at 25% 26%, rgba(235, 235, 232, 0.75) 0%, rgba(235, 235, 232, 0) 100%),
      radial-gradient(ellipse 35% 10% at 80% 14%, rgba(240, 240, 238, 0.8) 0%, rgba(240, 240, 238, 0) 100%),
      linear-gradient(180deg, var(--storm-grey) 0%, var(--storm-dark) 38%, #8d7a66 60%, var(--mist) 85%, #bdb8b0 100%);
  }
  .title {
    position: absolute;
    left: 0;
    top: 52px;
    width: 100%;
    text-align: center;
  }
  .title-main {
    display: block;
    font-family: "Oswald", "Arial Narrow", sans-serif;
    font-weight: 600;
    color: var(--title-orange);
    text-transform: uppercase;
    line-height: 0.92;
    text-shadow: 2px 3px 4px var(--text-shadow);
  }
  .title-peace {
    font-size: 148px;
    letter-spacing: 2px;
    margin-left: -60px;
  }
  .title-storms {
    font-size: 148px;
    letter-spacing: 1px;
    margin-top: -20px;
  }
  .title-link {
    position: relative;
    z-index: 2;
    display: block;
    font-family: "Cormorant Garamond", "Palatino Linotype", serif;
    font-style: italic;
    font-weight: 600;
    font-size: 66px;
    color: var(--script-white);
    line-height: 1;
    margin-top: -40px;
    margin-left: -30px;
    text-shadow: 2px 3px 4px var(--text-shadow);
  }
  .author-name {
    position: absolute;
    left: 0;
    width: 100%;
    top: 872px;
    text-align: center;
    font-family: "Cormorant Garamond", "Palatino Linotype", serif;
    font-style: italic;
    font-weight: 600;
    font-size: 62px;
    color: var(--script-white);
    text-shadow: 2px 3px 4px var(--text-shadow);
  }
</style>
</head>
<body>
  <div class="canvas">
    <div class="book-cover">
      <div class="cover-art" role="img" aria-label="Storm clouds parting around a radiant golden glow, a large luminous seated figure of light, and a lone man in silhouette standing on a bright path casting a long shadow"></div>
      <h1 class="title">
        <span class="title-main title-peace">Peace</span>
        <span class="title-link">Through The</span>
        <span class="title-main title-storms">Storms</span>
      </h1>
      <p class="author-name">Author’s Name</p>
    </div>
  </div>
</body>
</html>
```